Coffee Shop needs a fresh new menu

Hi,
I would like a new menu to be designed for our coffee shop.
We display our menu on a television screen, so would need it in a file that would allow us to continue to do so -- I have attached a photo so that you can see our current design, and how it is displayed.

I'd like something that is easy to read, if the design could have a "hipster" feel to it -- we are located at a hospital and University.

I have attached a Word file with what we would like on the menu.

Feel free to contact me if you have any questions.

Thanks,
Liv

Just A4 size will be fine, and no need to include menu 1 and menu 2 - I just put them in as an example of what we already have -- they are our printed menu's. Thanks

Hospital

```html
<!DOCTYPE html>
<html lang="en">
<head>
<meta charset="utf-8">
<title>Menu</title>
<link rel="stylesheet" href="https://fonts.googleapis.com/css2?family=Allura&family=Amatic+SC:wght@700&family=Over+the+Rainbow&display=swap">
<style>
  :root {
    --paper: #efe6dc;
    --wash: #ecd7c4;
    --panel: rgba(250, 246, 242, 0.82);
    --card: rgba(253, 247, 247, 0.9);
    --ink: #8a2d48;
    --ink-shadow: rgba(233, 120, 160, 0.55);
    --rose: #e0306f;
    --rose-soft: #f1a9c2;
    --gold: #c9ab8c;
    --tile: #d9b0a8;
    --band: #d8cfcb;
  }
  html, body { margin: 0; padding: 0; overflow: hidden; }
  body { width: 847px; height: 1200px; }
  .canvas {
    position: relative; width: 847px; height: 1200px; overflow: hidden;
    background:
      radial-gradient(ellipse at 15% 40%, rgba(222, 170, 130, 0.35), transparent 55%),
      radial-gradient(ellipse at 85% 15%, rgba(230, 190, 160, 0.3), transparent 50%),
      var(--paper);
  }
  .floor-band {
    position: absolute; left: 0; top: 881px; width: 847px; height: 319px;
    background: linear-gradient(180deg, #ddd2cc, var(--band));
  }
  .sheet {
    position: absolute; left: 53px; top: 38px; width: 742px; height: 1114px;
    background: var(--panel);
  }
  .title {
    position: absolute; left: 0; top: 52px; width: 847px; text-align: center;
    font-family: "Allura", cursive; font-size: 128px; line-height: 1;
    color: var(--rose); text-shadow: 2px 3px 2px rgba(120, 60, 80, 0.35);
  }
  .title-wash {
    position: absolute; left: 330px; top: 55px; width: 260px; height: 160px;
    background: radial-gradient(ellipse, rgba(240, 170, 195, 0.45), transparent 70%);
  }
  .card {
    position: absolute; background: var(--card);
    box-shadow: 0 0 0 8px rgba(255, 255, 255, 0.55);
  }
  .card-light { left: 188px; top: 218px; width: 444px; height: 489px; }
  .card-breakfast {
    left: 86px; top: 739px; width: 670px; height: 379px;
    box-shadow: 0 0 0 10px rgba(225, 205, 198, 0.8);
  }
  .section-head {
    position: absolute; font-family: "Over the Rainbow", cursive;
    font-size: 30px; color: var(--ink); letter-spacing: 1px; white-space: nowrap;
  }
  .head-light { left: 188px; width: 444px; top: 230px; text-align: center; }
  .head-breakfast { right: 119px; top: 740px; }
  .menu-list { position: absolute; margin: 0; padding: 0; list-style: none; }
  .menu-list li {
    display: flex; justify-content: space-between;
    font-family: "Amatic SC", sans-serif; font-weight: 700; color: var(--ink);
    text-shadow: 2px 2px 0 var(--ink-shadow); white-space: nowrap;
  }
  .list-light { left: 258px; top: 295px; width: 314px; }
  .list-light li { font-size: 40px; line-height: 48.8px; letter-spacing: 3px; }
  .list-breakfast { left: 112px; top: 792px; width: 377px; }
  .list-breakfast li { font-size: 31px; line-height: 36.5px; letter-spacing: 2px; }
  .list-extras { left: 500px; top: 970px; width: 252px; }
  .list-extras li { font-size: 31px; line-height: 36.5px; letter-spacing: 2px; justify-content: flex-end; gap: 20px; }
  .list-extras .price { width: 57px; text-align: right; }
  .photo-frame {
    position: absolute; left: 595px; width: 197px; height: 158px; box-sizing: border-box;
    border: 9px solid var(--gold);
    background: linear-gradient(120deg, #f4dde3, #e98aa9 55%, #f3d6dd);
  }
  .frame-top { top: 295px; }
  .frame-bottom { top: 476px; }
  .tile {
    position: absolute; height: 78px;
    background: linear-gradient(135deg, #ddbcaf, var(--tile) 60%, #e4c2bb);
  }
  .petals {
    position: absolute; left: 60px; top: 593px; width: 275px; height: 152px;
    background:
      radial-gradient(ellipse at 58% 35%, rgba(224, 48, 111, 0.85), transparent 40%),
      radial-gradient(ellipse at 25% 80%, rgba(224, 48, 111, 0.75), transparent 38%);
  }
</style>
</head>
<body>
<main class="canvas">
  <div class="floor-band"></div>
  <div class="sheet"></div>

  <div class="tile" style="left:794px; top:854px; width:53px;"></div>
  <div class="tile" style="left:0; top:1006px; width:49px;"></div>

  <div class="title-wash" role="img" aria-label="Soft watercolour peony behind the heading"></div>
  <h1 class="title" style="margin:0; font-weight:400;">Menu</h1>

  <section class="card card-light"></section>
  <h2 class="section-head head-light" style="margin:0; font-weight:400;">-something light-</h2>
  <ul class="menu-list list-light">
    <li><span>Mixed yoghurts</span><span>$5.50</span></li>
    <li><span>Chia pudding</span><span>$5.50</span></li>
    <li><span>Fruit salad</span><span>$5.50</span></li>
    <li><span>Bircher muesli</span><span>$5.50</span></li>
    <li><span>Protein balls</span><span>$4.0</span></li>
    <li><span>Banana bread</span><span>$4.50</span></li>
    <li><span>Muffins</span><span>$4.50</span></li>
    <li><span>Slices</span><span>$4.0</span></li>
  </ul>

  <div class="photo-frame frame-top" role="img" aria-label="Framed photo of a pink peony"></div>
  <div class="photo-frame frame-bottom" role="img" aria-label="Framed photo of pink roses"></div>

  <section class="card card-breakfast"></section>
  <div class="tile" style="left:498px; top:854px; width:138px;"></div>
  <div class="tile" style="left:646px; top:854px; width:138px;"></div>
  <div class="tile" style="left:58px; top:1006px; width:139px;"></div>
  <div class="tile" style="left:208px; top:1006px; width:138px;"></div>

  <div class="petals" role="img" aria-label="Scattered pink rose petals"></div>

  <h2 class="section-head head-breakfast" style="margin:0; font-weight:400;">-breakfast items-</h2>
  <ul class="menu-list list-breakfast">
    <li><span>Bacon, egg and cheese roll</span><span>$6.0</span></li>
    <li><span>Ham and cheese toastie</span><span>$5.0</span></li>
    <li><span>Cheese and tomato toastie</span><span>$5.0</span></li>
    <li><span>Ham and cheese croissant</span><span>$6.0</span></li>
    <li><span>Cheese and tomato croissant</span><span>$5.50</span></li>
  </ul>
  <ul class="menu-list list-extras">
    <li><span>Plain croissant</span><span class="price">$3.50</span></li>
    <li><span>Hash brown</span><span class="price">$2.0</span></li>
    <li><span>2 piece toast</span><span class="price">$3.0</span></li>
    <li><span>2 piece rasin toast</span><span class="price">$3.0</span></li>
  </ul>
</main>
</body>
</html>
```